Property development & Investment company Need a logo & business card design

Our name is KT Estates Australia Pty Ltd
Need logo & business card design

Target Market(s)

People dealing in commercial property

Industry/Entity Type

Business

Contact Information for Business Card

KT Estates Australia
Peter Moss Mobile0419 703 646
Email Peter@birchvale-sample.com.au

Font styles to use
Sans Serif

Requirements
Must have
• company name
• contact details
Nice to have
• KT Estates Bold
• Australia Not Bold
Should not have
• To busy of a look

```html
<!DOCTYPE html>
<html lang="en">
<head>
<meta charset="utf-8">
<title>KT Estates Australia – Business Card</title>
<link rel="stylesheet" href="https://fonts.googleapis.com/css2?family=Montserrat:wght@600;700&family=Lato:wght@400;700&display=swap">
<style>
  :root {
    --backdrop: #2b2b2b;
    --card: #f4f4f4;
    --navy: #123f73;
    --ink: #333333;
    --charcoal: #2a2a2a;
    --rule: #444444;
  }
  * { box-sizing: border-box; margin: 0; padding: 0; }
  html, body { width: 1200px; height: 873px; overflow: hidden; }
  body {
    background: var(--backdrop);
    display: flex;
    align-items: center;
    justify-content: center;
  }
  .business-card {
    position: relative;
    width: 1000px;
    height: 571px;
    background: var(--card);
    overflow: hidden;
    box-shadow: 0 20px 50px rgba(0,0,0,.5);
  }
  .brand {
    position: absolute;
    left: 110px;
    top: 150px;
    display: flex;
    flex-direction: column;
    gap: 12px;
  }
  .brand-name {
    display: flex;
    align-items: center;
    gap: 14px;
    font-family: 'Montserrat', sans-serif;
    font-weight: 700;
    font-size: 38px;
    color: var(--navy);
    letter-spacing: .5px;
  }
  .brand-square {
    width: 22px;
    height: 22px;
    background: var(--navy);
  }
  .tagline {
    display: flex;
    align-items: center;
    gap: 12px;
    margin-left: 36px;
    font-family: 'Lato', sans-serif;
    font-size: 17px;
    color: var(--navy);
  }
  .tagline::before, .tagline::after {
    content: "";
    width: 50px;
    height: 2px;
    background: var(--rule);
  }
  .person {
    position: absolute;
    right: 90px;
    top: 245px;
    text-align: right;
  }
  .person-name {
    font-family: 'Lato', sans-serif;
    font-weight: 700;
    font-size: 28px;
    color: var(--navy);
  }
  .person-role {
    font-family: 'Lato', sans-serif;
    font-weight: 700;
    font-size: 17px;
    color: var(--ink);
    margin-top: 2px;
  }
  .contact-list {
    position: absolute;
    left: 110px;
    top: 405px;
    list-style: none;
    display: flex;
    flex-direction: column;
    gap: 18px;
  }
  .contact-item {
    display: flex;
    align-items: center;
    gap: 18px;
    font-family: 'Lato', sans-serif;
    font-weight: 700;
    font-size: 22px;
    color: var(--ink);
    letter-spacing: .5px;
  }
  .contact-icon { width: 22px; height: 22px; flex: none; }
  .card-bands {
    position: absolute;
    left: 0;
    bottom: 0;
    width: 1000px;
    height: 70px;
  }
</style>
</head>
<body>
  <div class="business-card">
    <div class="brand">
      <div class="brand-name"><span class="brand-square"></span>KT Estates Australia Pty Ltd</div>
      <div class="tagline">Property Development &amp; Investment Company</div>
    </div>

    <div class="person">
      <div class="person-name">Peter Moss</div>
      <div class="person-role">Director</div>
    </div>

    <ul class="contact-list">
      <li class="contact-item">
        <svg class="contact-icon" viewBox="0 0 22 22" aria-hidden="true">
          <rect x="5" y="1" width="12" height="20" rx="2" fill="none" stroke="#123f73" stroke-width="2"/>
          <circle cx="11" cy="17" r="1.3" fill="#123f73"/>
        </svg>
        0455 218 907
      </li>
      <li class="contact-item">
        <svg class="contact-icon" viewBox="0 0 22 22" aria-hidden="true">
          <rect x="1" y="4" width="20" height="14" fill="#123f73"/>
          <path d="M1 4 L11 12 L21 4" fill="none" stroke="#f4f4f4" stroke-width="1.5"/>
        </svg>
        Peter@birchvale-sample.com.au
      </li>
    </ul>

    <svg class="card-bands" viewBox="0 0 1000 70" aria-hidden="true">
      <path d="M0 50 H600 Q620 50 628 36 L640 36 Q632 54 640 70 H0 Z" fill="#2a2a2a"/>
      <path d="M660 70 Q650 30 700 30 H1000 V70 Z" fill="#123f73"/>
      <path d="M640 70 Q630 22 700 18 H1000 V30 H700 Q650 30 660 70 Z" fill="#f4f4f4"/>
    </svg>
  </div>
</body>
</html>
```